Business Card and Membership Card Design

Hi there.
This is Martin from Q-motion Sports Club. I would like to design a business card for myself. Q-motion Sports Club is a recreational sports club, we do basketball, badminton, table tennis and 8 ball pool. At this moment, I've a club business card and a loyalty card but I need a new format business for myself as a General Manager at the club and also a design for my club membership card. Can you please reply my email and I'll send the detailed description of what I'd like to do?
The email address is martinhaowenpell@mailorbit-post.com

Target Market(s)

Recreational Sports, Social Sports Activity. Basketball, Indoor Soccer, Badminton Table Tennis.
Group booking, Event Hosting, Holiday Program, Sports Coaching, Kids program. birthday party

Industry/Entity Type

Recreation

Contact Information for Business Card

Name: Q-motion Sports
Slogan: Play with passion
General Manager: Martin Pell
Contact: 022 0561938
Weichat: martinhaowenpell
Company Address: Unit 7, 19 Kestrel Avenue, New Lynn, Auckland.
Email: martinhaowenpell@mailorbit-post.com
And on the back of the card:
Basketball
Indoor Soccer
Badminton
Table Tennis
Group / Company Booking
Event Hosting
Birthday Party
Holiday Program
Kids Training

Font styles to use
Sans Serif

Requirements
Must have
• My project must have all of the information and clear details.
• I'd like to make the format simple and looks smart.
• As a sports club, I prefer this design looks like positive, power, and moden
Nice to have
• As a sports club, I prefer this design looks like positive, power, and modern
• Probably make this design in a black card and the edge side is around.

```html
<!DOCTYPE html>
<html lang="en">
<head>
<meta charset="utf-8">
<title>Q-motion Sports – Business Card</title>
<link href="https://fonts.googleapis.com/css2?family=Open+Sans:wght@400;600;700&display=swap" rel="stylesheet">
<style>
  :root {
    --backdrop: #e8e5e2;
    --card-white: #ffffff;
    --card-dark: #262626;
    --band-dark: #222222;
    --ink: #111111;
    --ink-soft: #2a2a2a;
    --rule: #555555;
    --paper-text: #f2f2f2;
    --fern-tone: #303030;
  }
  * { box-sizing: border-box; margin: 0; padding: 0; }
  html, body {
    width: 1200px;
    height: 900px;
    overflow: hidden;
    background: var(--backdrop);
    font-family: "Open Sans", sans-serif;
  }
  .canvas { position: relative; width: 1200px; height: 900px; }

  .card {
    position: absolute;
    width: 560px;
    height: 347px;
    border-radius: 18px;
    overflow: hidden;
    box-shadow: 0 6px 18px rgba(0,0,0,0.12);
  }
  .card--front { left: 145px; top: 115px; background: var(--card-white); }
  .card--back  { left: 547px; top: 503px; background: var(--card-dark); }

  .brand-name {
    position: absolute;
    left: 0; right: 0;
    text-align: center;
    font-family: "Open Sans", sans-serif;
    font-weight: 700;
    font-size: 32px;
    line-height: 40px;
    letter-spacing: 0.5px;
  }
  .card--front .brand-name { top: 82px; color: var(--ink); }
  .card--back .brand-name  { top: 72px; color: var(--paper-text); }

  .person {
    position: absolute;
    right: 318px;
    top: 174px;
    text-align: right;
    color: var(--ink-soft);
  }
  .person__name { font-weight: 700; font-size: 17px; line-height: 22px; color: var(--ink); }
  .person__role { font-size: 14.5px; line-height: 20px; }

  .divider {
    position: absolute;
    left: 257px;
    top: 178px;
    width: 1px;
    height: 38px;
    background: var(--rule);
  }

  .address {
    position: absolute;
    left: 272px;
    top: 175px;
    font-size: 14.5px;
    line-height: 21px;
    color: var(--ink-soft);
  }

  .contact-line {
    position: absolute;
    left: 0; right: 0;
    top: 232px;
    text-align: center;
    font-size: 14px;
    color: var(--ink-soft);
  }
  .contact-line b { font-weight: 700; color: var(--ink); }
  .contact-line .sep { margin: 0 5px; }

  .slogan-band {
    position: absolute;
    left: 0; right: 0; bottom: 0;
    height: 65px;
    background: var(--band-dark);
    color: var(--paper-text);
    display: flex;
    align-items: center;
    justify-content: center;
    font-weight: 700;
    font-size: 18px;
    letter-spacing: 2.4px;
    text-transform: uppercase;
  }

  .fern-decoration {
    position: absolute;
    left: 300px;
    top: 130px;
    width: 90px;
    height: 250px;
    border-radius: 50%;
    background: linear-gradient(180deg, var(--fern-tone), rgba(48,48,48,0.4));
    transform: rotate(38deg);
  }

  .services {
    position: absolute;
    left: 64px;
    top: 146px;
    list-style: none;
    color: var(--paper-text);
    font-size: 16.5px;
    line-height: 25.5px;
  }
  .services li { position: relative; padding-left: 13px; }
  .services li::before {
    content: "";
    position: absolute;
    left: 0; top: 11px;
    width: 6px; height: 6px;
    border-radius: 50%;
    background: var(--paper-text);
  }
</style>
</head>
<body>
<main class="canvas">

  <section class="card card--front" aria-label="Business card front">
    <h1 class="brand-name">Q-motion Sports</h1>
    <div class="person">
      <p class="person__name">MARTIN PELL</p>
      <p class="person__role">General Manager</p>
    </div>
    <span class="divider"></span>
    <p class="address">Unit 7, 19 Kestrel Avenue,<br>New Lynn, AKL.</p>
    <p class="contact-line"><b>P:</b> 022 0561938<span class="sep">|</span><b>E:</b> martinhaowenpell@mailorbit-post.com</p>
    <div class="slogan-band">Play with passion</div>
  </section>

  <section class="card card--back" aria-label="Business card back">
    <div class="fern-decoration" role="img" aria-label="Faint leaf decoration"></div>
    <h2 class="brand-name">Q-motion Sports</h2>
    <ul class="services">
      <li>Basketball and Indoor Soccer</li>
      <li>Badminton and Table Tennis</li>
      <li>Group / Company Booking</li>
      <li>Event Hosting and Birthday Party</li>
      <li>Holiday Program</li>
      <li>Kids Training</li>
    </ul>
  </section>

</main>
</body>
</html>
```